Advertising flyer for proofreading business.

Hello everyone,

I need an advertising flyer for a new proofreading company in Australia.

I would like your design in be in two sizes:
- A4 (to be posted on noticeboards),
- A6 (to be printed in larger quantity to give away)
(please see the size specification file attached).

The text file is attached (Ad Text) and it contains lots of information. Please feel free to include your choice of text from the text file, but please include Poster title, and highlight 'ESL' and students discounts.

I understand that it is impossible to include the same amount of information on A6 and A4, so please feel free to chose what fits on each of them, but please keep the design similar.

I have attached our company logo, but feel free to adjust it to the poster design (feel free to change the color as well). The original logo file contains circle around it, please feel free to remove it and include only the typeset as it can be seen here: http://www.vellumcheck.com.au/.

Flyers will be printed, so please see the specification file for details.

I will do my best to respond to feedback as soon as possible.

I appreciate your participation, time and help,
Best wishes,
Radoslaw

Target Market(s)

Students, authors

Industry/Entity Type

Business

Colors

Designer to choose colors to be used in the design.

Requirements
Must have
• It would be good if poster is easy to spot on busy noticeboards and attract attention.
• Please keep the poster in the positive/optimistic mood, and so that it focuses on students, maybe photos of graduates(?).
• Poster title,
• Please include the list of proof-read documents as they are described in the attached text file (Ad Text).
• Please highlight students discounts and ESL.
Nice to have
• I would like to leave the creative freedom to all designers so at this point I have not adjusted the Look and Feel sliders. Please feel free to offer your own take on this.
• It would be nice if most of the text could be fit to the poster.

```html
<!DOCTYPE html>
<html lang="en">
<head>
<meta charset="utf-8">
<title>Vellumcheck – Professional English Language Proofreading</title>
<link rel="stylesheet" href="https://fonts.googleapis.com/css2?family=Arimo&family=Open+Sans:wght@300;400;700&family=Crimson+Text&family=Oswald:wght@500;700&family=Delius+Swash+Caps&family=Roboto:wght@500&display=swap">
<style>
  :root {
    --teal: #64c1b3;
    --teal-dark: #3f8d84;
    --ink: #2d2d2d;
    --black: #111;
    --white: #fff;
    --ring: #e6ecec;
    --photo-green: #8fae6a;
    --photo-warm: #c9a583;
  }
  * { box-sizing: border-box; margin: 0; padding: 0; }
  h1, h2, h3 { font-weight: 400; }
  html, body { width: 873px; height: 1200px; overflow: hidden; background: var(--white); }
  .flyer { position: relative; width: 873px; height: 1200px; background: var(--white); overflow: hidden; }

  .side-panel { position: absolute; left: 503px; top: 0; width: 370px; height: 1200px; background: var(--teal); }

  .title {
    position: absolute; left: 38px; top: 46px;
    font-family: "Arimo", sans-serif; color: var(--ink);
    font-size: 49px; line-height: 61px;
  }

  .student-photo {
    position: absolute; left: 0; top: 318px; width: 503px; height: 355px;
    background: linear-gradient(135deg, var(--photo-green) 0%, #b9c98f 35%, var(--photo-warm) 70%, #6f9fbf 100%);
  }

  .badge-circle { position: absolute; left: 0; top: 0; width: 873px; height: 1200px; }

  .esl {
    position: absolute; left: 503px; top: 42px; width: 370px; text-align: center;
    font-family: "Open Sans", sans-serif; font-weight: 300; color: var(--white);
    font-size: 50px; line-height: 58px;
  }

  .brand {
    position: absolute; left: 430px; top: 494px; width: 390px; text-align: center;
    font-family: "Open Sans", sans-serif; font-weight: 300; color: var(--white);
    font-size: 62px; line-height: 80px; letter-spacing: -1px;
  }
  .brand-dot {
    display: inline-block; width: 22px; height: 22px; border-radius: 50%;
    background: var(--black); margin-right: 10px; vertical-align: middle;
  }

  .credentials {
    position: absolute; left: 503px; top: 667px; width: 370px; text-align: center;
    font-family: "Open Sans", sans-serif; font-weight: 700; color: var(--white);
    font-size: 19px; line-height: 28.5px; text-shadow: 0 1px 2px rgba(0,0,0,.25);
  }

  .testimonial-heading {
    position: absolute; left: 503px; top: 786px; width: 370px; text-align: center;
    font-family: "Delius Swash Caps", cursive; color: var(--white); font-size: 31px; line-height: 40px;
  }
  .testimonial-quote {
    position: absolute; left: 522px; top: 837px; width: 330px;
    text-align: justify; text-align-last: center;
    font-family: "Open Sans", sans-serif; font-weight: 300; color: var(--white);
    font-size: 15px; line-height: 22.5px;
  }
  .testimonial-name {
    position: absolute; left: 503px; top: 937px; width: 370px; text-align: center;
    font-family: "Delius Swash Caps", cursive; color: var(--white); font-size: 29px; line-height: 34px;
  }
  .testimonial-role {
    position: absolute; left: 503px; top: 971px; width: 370px; text-align: center;
    font-family: "Delius Swash Caps", cursive; color: var(--white); font-size: 15px; line-height: 20px;
  }

  .contact-heading {
    position: absolute; left: 503px; top: 1030px; width: 370px; text-align: center;
    font-family: "Roboto", sans-serif; font-weight: 500; color: var(--black);
    font-size: 33px; line-height: 42px; letter-spacing: .5px;
  }
  .contact-phone {
    position: absolute; left: 503px; top: 1075px; width: 370px; text-align: center;
    font-family: "Oswald", sans-serif; font-weight: 700; color: var(--white); font-size: 52px; line-height: 70px;
    text-shadow: 0 2px 3px rgba(0,0,0,.3);
  }
  .contact-email {
    position: absolute; left: 503px; top: 1143px; width: 370px; text-align: center;
    font-family: "Open Sans", sans-serif; font-weight: 700; color: var(--black); font-size: 19px; line-height: 26px;
  }

  .section-tab { position: absolute; left: 0; top: 660px; }
  .section-tab-label {
    position: absolute; left: 38px; top: 662px;
    font-family: "Crimson Text", serif; color: var(--white); font-size: 23px; line-height: 30px;
  }

  .doc-list {
    position: absolute; left: 38px; top: 701px; list-style: none;
    font-family: "Crimson Text", serif; color: var(--ink); font-size: 15.5px; line-height: 19.3px;
  }
  .doc-list li { display: flex; align-items: center; gap: 7px; }
  .doc-list svg { flex: none; }

  .price-heading {
    position: absolute; left: 38px; top: 949px;
    font-family: "Crimson Text", serif; color: var(--teal-dark); font-size: 23px; line-height: 30px; letter-spacing: .3px;
  }
  .price-list {
    position: absolute; left: 38px; top: 988px; width: 350px; list-style: none;
    font-family: "Crimson Text", serif; color: var(--ink); font-size: 14px; line-height: 17px;
  }
  .price-list li { position: relative; padding-left: 21px; margin-bottom: 6px; }
  .price-list li::before {
    content: ""; position: absolute; left: 2px; top: 4px; width: 10px; height: 10px; border-radius: 50%;
    background: radial-gradient(circle at 35% 35%, #9be0d4, var(--teal-dark));
  }

  .website {
    position: absolute; left: 38px; top: 1139px;
    font-family: "Oswald", sans-serif; font-weight: 500; color: var(--teal-dark);
    font-size: 24px; line-height: 34px; letter-spacing: 2.5px;
  }
</style>
</head>
<body>
<main class="flyer">
  <div class="side-panel"></div>

  <h1 class="title">PROFESSIONAL<br>ENGLISH<br>LANGUAGE<br>PROOFREADING</h1>

  <div class="student-photo" role="img" aria-label="Photo of a group of smiling university students studying together outdoors with a laptop and notebooks"></div>

  <svg class="badge-circle" viewBox="0 0 873 1200" aria-hidden="true">
    <defs>
      <clipPath id="panel-edge"><rect x="0" y="0" width="503" height="1200"/></clipPath>
    </defs>
    <circle cx="595" cy="496" r="206" fill="var(--teal)" stroke="var(--ring)" stroke-width="6" clip-path="url(#panel-edge)"/>
  </svg>

  <h2 class="esl">Help with<br>English as a<br>Second<br>Language<br>(ESL)</h2>

  <div class="brand"><span class="brand-dot"></span>Vellumcheck</div>

  <p class="credentials">Proofreading by a native<br>English speaker with an<br>Honours degree in English.</p>

  <h3 class="testimonial-heading">Testimonial</h3>
  <p class="testimonial-quote">“Harriet understood” our requirements quickly and has been fantastic at delivering quality work, on time and within an agreed budget. please to work with her.</p>
  <p class="testimonial-name">Carol Duncan</p>
  <p class="testimonial-role">Operations Manager, Northvale</p>

  <h3 class="contact-heading">CONTACT HARRIET</h3>
  <p class="contact-phone">0400 555 218</p>
  <p class="contact-email">proofing@vellumcheck.com.au</p>

  <svg class="section-tab" width="316" height="34" viewBox="0 0 316 34" aria-hidden="true">
    <polygon points="0,0 316,0 302,34 0,34" fill="var(--teal-dark)"/>
  </svg>
  <h3 class="section-tab-label">Documents include:</h3>

  <ul class="doc-list">
    <li><svg width="12" height="10" viewBox="0 0 12 10"><path d="M1 5 L4.5 8.5 L11 1" fill="none" stroke="var(--teal-dark)" stroke-width="2"/></svg>Essays and assignments</li>
    <li><svg width="12" height="10" viewBox="0 0 12 10"><path d="M1 5 L4.5 8.5 L11 1" fill="none" stroke="var(--teal-dark)" stroke-width="2"/></svg>Theses</li>
    <li><svg width="12" height="10" viewBox="0 0 12 10"><path d="M1 5 L4.5 8.5 L11 1" fill="none" stroke="var(--teal-dark)" stroke-width="2"/></svg>Resumes</li>
    <li><svg width="12" height="10" viewBox="0 0 12 10"><path d="M1 5 L4.5 8.5 L11 1" fill="none" stroke="var(--teal-dark)" stroke-width="2"/></svg>Business correspondence</li>
    <li><svg width="12" height="10" viewBox="0 0 12 10"><path d="M1 5 L4.5 8.5 L11 1" fill="none" stroke="var(--teal-dark)" stroke-width="2"/></svg>Training manuals</li>
    <li><svg width="12" height="10" viewBox="0 0 12 10"><path d="M1 5 L4.5 8.5 L11 1" fill="none" stroke="var(--teal-dark)" stroke-width="2"/></svg>Newsletters</li>
    <li><svg width="12" height="10" viewBox="0 0 12 10"><path d="M1 5 L4.5 8.5 L11 1" fill="none" stroke="var(--teal-dark)" stroke-width="2"/></svg>Advertising copy</li>
    <li><svg width="12" height="10" viewBox="0 0 12 10"><path d="M1 5 L4.5 8.5 L11 1" fill="none" stroke="var(--teal-dark)" stroke-width="2"/></svg>Brochures, catalogues</li>
    <li><svg width="12" height="10" viewBox="0 0 12 10"><path d="M1 5 L4.5 8.5 L11 1" fill="none" stroke="var(--teal-dark)" stroke-width="2"/></svg>media releases</li>
    <li><svg width="12" height="10" viewBox="0 0 12 10"><path d="M1 5 L4.5 8.5 L11 1" fill="none" stroke="var(--teal-dark)" stroke-width="2"/></svg>Websites</li>
    <li><svg width="12" height="10" viewBox="0 0 12 10"><path d="M1 5 L4.5 8.5 L11 1" fill="none" stroke="var(--teal-dark)" stroke-width="2"/></svg>Presentations and speeches</li>
    <li><svg width="12" height="10" viewBox="0 0 12 10"><path d="M1 5 L4.5 8.5 L11 1" fill="none" stroke="var(--teal-dark)" stroke-width="2"/></svg>Novels and short stories</li>
  </ul>

  <h3 class="price-heading">PRICE GUIDE:</h3>
  <ul class="price-list">
    <li>Discounts for not-for-profit organisations.</li>
    <li>Great student discount rate: $25 per hour (roughly<br>1000 words - 4 pages - of well-written text).</li>
    <li>Package deals on documents over 50,000 words.</li>
    <li>Fast, negotiable time frames.</li>
    <li>(Same day service available by special arrangement).</li>
  </ul>

  <p class="website">www.vellumcheck.com.au</p>
</main>
</body>
</html>
```